Professional Business Card for a Chief Operating Officer

An exciting business card that's professional for a c-suite position.
Parent company on the front with information. (CLEAR HARBOR)
3 Brands on the back in a dark blue background.

No icons for phone, email or address.
The card can be vertically laid out or horizontally, whichever fits best.

I'd like to see designs in both formats.
Cards can be designed with a "linen" look or embossed with tone-on-tone as an option.

Target Market(s)

Industry professionals, customers and vendors

Industry/Entity Type

Car Wash

Contact Information for Business Card

Name, title, address, phone, email and logo

Colors
0054AA
0677BA
7BADD7
CADEEF
E8F1F8

Requirements
Must have
• A professional conservative look
Nice to have
• Parent Brand on front, Brand logos on back
Should not have
• Icons

```html
<!DOCTYPE html>
<html lang="en">
<head>
<meta charset="UTF-8">
<title>Clear Harbor Business Card</title>
<link rel="stylesheet" href="https://fonts.googleapis.com/css2?family=Montserrat:wght@400;500;700;800&display=swap">
<style>
  :root {
    --navy: #15214a;
    --brand-blue: #4a8bd0;
    --deep-blue: #0054aa;
    --sky: #7badd7;
    --mist: #e8f1f8;
    --accent: #f2a72e;
    --ink: #3a3f4a;
    --white: #ffffff;
    --stage: #d9dde3;
  }
  * { box-sizing: border-box; margin: 0; padding: 0; }
  html, body { width: 1200px; height: 900px; overflow: hidden; }
  body {
    background: var(--stage);
    font-family: 'Montserrat', sans-serif;
    position: relative;
  }
  .card {
    position: absolute;
    width: 700px;
    height: 400px;
    border-radius: 26px;
    overflow: hidden;
    box-shadow: 0 14px 30px rgba(0,0,0,0.22);
  }
  .card-back { left: 150px; top: 30px; background: var(--navy); }
  .card-front { left: 350px; top: 470px; background: var(--white); }
  .card svg.art { position: absolute; inset: 0; }

  .brand {
    position: absolute;
    font-weight: 800;
    letter-spacing: 1px;
    display: flex;
    align-items: center;
    gap: 12px;
    white-space: nowrap;
  }
  .brand-dot { border-radius: 50%; flex: none; }
  .brand-northwind { left: 60px; top: 220px; color: var(--white); font-size: 28px; }
  .brand-northwind .brand-dot { width: 22px; height: 22px; background: var(--accent); }
  .brand-finish { left: 350px; top: 42px; color: var(--white); font-size: 19px; }
  .brand-bright { left: 400px; top: 240px; color: var(--brand-blue); font-size: 30px; letter-spacing: 3px; font-weight: 500; }
  .brand-bright .brand-dot { width: 26px; height: 26px; border: 4px solid var(--brand-blue); }

  .brand-parent { right: 48px; top: 38px; color: var(--brand-blue); font-size: 30px; }
  .brand-parent .brand-dot { width: 56px; height: 56px; background: var(--brand-blue); }

  .person { position: absolute; left: 46px; top: 128px; }
  .person-name { color: var(--brand-blue); font-weight: 700; font-size: 26px; letter-spacing: 1.5px; }
  .person-title { color: var(--ink); font-weight: 400; font-size: 18px; margin-top: 2px; }

  .contact {
    position: absolute;
    left: 170px;
    top: 262px;
    color: var(--white);
    font-size: 16px;
    line-height: 1.35;
    font-weight: 400;
  }
  .contact-group + .contact-group { margin-top: 8px; }
</style>
</head>
<body>

<section class="card card-back" aria-label="Brand card back">
  <svg class="art" viewBox="0 0 700 400" width="700" height="400" aria-hidden="true">
    <g stroke="var(--accent)" stroke-width="3" fill="none">
      <line x1="70" y1="0" x2="330" y2="165"/>
      <line x1="330" y1="165" x2="700" y2="70"/>
      <line x1="330" y1="165" x2="250" y2="400"/>
    </g>
  </svg>
  <div class="brand brand-finish">FINE FINISH DETAILING</div>
  <div class="brand brand-northwind"><span class="brand-dot"></span>NORTHWIND</div>
  <div class="brand brand-bright"><span class="brand-dot"></span>BRIGHTWAY</div>
</section>

<section class="card card-front" aria-label="Clear Harbor contact card">
  <svg class="art" viewBox="0 0 700 400" width="700" height="400" aria-hidden="true">
    <path d="M0 300 C 120 170, 260 220, 420 210 C 560 200, 640 150, 700 95 L700 118 C 640 175, 560 222, 420 230 C 280 238, 140 200, 0 330 Z" fill="var(--brand-blue)"/>
    <path d="M0 345 C 140 210, 280 248, 420 240 C 560 232, 640 190, 700 130 L700 400 L0 400 Z" fill="var(--navy)"/>
  </svg>
  <div class="brand brand-parent"><span class="brand-dot"></span>CLEAR HARBOR</div>
  <div class="person">
    <div class="person-name">DANIEL MERCER</div>
    <div class="person-title">Chief Operating Officer</div>
  </div>
  <div class="contact">
    <div class="contact-group">
      <p>880 Harbor View Rd Ste 12</p>
      <p>Portland OR 97201</p>
    </div>
    <div class="contact-group">
      <p>(503) 555 0148</p>
      <p>info@clearharborwash.com</p>
      <p>www.clearharborwash.com</p>
    </div>
  </div>
</section>

</body>
</html>
```